Etiketten für Tees
Zielgruppe
Wir sind eine klassische Foto-Drogerie mit traditioneller Likör Herstellung, Tee- und Gewürzstube mit offenen und selbst abgepackten Spezialitäten. Süßwarenabteilung mit Confiserie, großer Bonbon Auswahl und Drogerie Grundsortiment.
Wir suchen ein neues Etiketten Design für unsere selbst abgepackten Tees, Bonbons und Gewürze.
Aufgabenstellung
Die Etiketten für die Tees sollten durch verschiedene Farben oder Grafiken in die nachfolgenden Kategorien unterscheidbar sein: Schwarzer Tee, Grüner Tee, Früchte Tee, Rooibusch Tee und Kräuter Tee.
Abgefüllt sind die Tees in Blockbeutel Natron natur und die Früchtetees in Klarsichtbeutel.
Die Etiketten sollten etwa 65mm breit sein. die Länge kann zwischen 70mm und 110mm betragen.
Folgene Information müsste aufgedruckt werden: Art (Schwarzer Tee), Sorte (Darjeeling), kurze Beschreibung oder Geschmack (Erdbeer Geschmack), Füllmenge sowie unser Logo mit Adresse. Die Inhaltsstoffe, Zubereitung, Nährwerttabelle kommen in Text oder Tabellenform auf die Rückseite auf ein neutrales Etikett (hier nicht zu berücksichtigen).
Die Etiketten wollen wir mit unserem hochwertigen Vollfarb Etikettendrucker selbst ausdrucken (Drucker Velorix).
Das Design sollte auf die Natron Beutel farblich und von der Gestaltung her abgestimmt sein (natürliches und qualitativ hochwertiges Produkt - keine Massenware vom Discounter, jedoch trotzdem modern und 'nicht angestaubt spießig', aber nicht zu grelle Farben).
Wir möchten diese Etiketten im Sinne eines stimmigen Gesamtauftritts (sh. Foto) auch für unsere selbst abgepackten Bonbons und Gewürze verwenden. Es unterscheidet sich also nur marginal, d.h. in Bezeichnung und Füllmenge. Logo und Adresse bzw. das Gesamtbild sollen also gleich sein.

```html
<!DOCTYPE html>
<html lang="de">
<head>
<meta charset="utf-8">
<title>Kelmbach Etiketten</title>
<link href="https://fonts.googleapis.com/css2?family=Kaushan+Script&family=Libre+Baskerville:wght@400;700&display=swap" rel="stylesheet">
<style>
  :root {
    --canvas: #efefef;
    --label: #ffffff;
    --ink: #1f1f1f;
    --ink-soft: #2b2b2b;
    --gold-light: #e6d39e;
    --gold: #cdab55;
    --pink-light: #efb3d6;
    --pink: #e07cbd;
    --pink-text: #d1358f;
    --blue-light: #bcd8f2;
    --blue: #8dbde9;
    --script: "Kaushan Script", cursive;
    --serif: "Libre Baskerville", serif;
  }
  * { box-sizing: border-box; margin: 0; padding: 0; }
  html, body { width: 1200px; height: 800px; overflow: hidden; }
  body { background: var(--canvas); position: relative; font-family: var(--serif); color: var(--ink); }

  .label { position: absolute; background: var(--label); overflow: hidden; box-shadow: 0 1px 3px rgba(0,0,0,.12); }
  .label--oregano { left: 101px; top: 429px; width: 186px; height: 201px; }
  .label--salbei  { left: 362px; top: 336px; width: 192px; height: 326px; }
  .label--vanille { left: 631px; top: 354px; width: 201px; height: 216px; }
  .label--bonbon  { left: 880px; top: 472px; width: 200px; height: 217px; }

  .swoosh { position: absolute; left: 0; width: 100%; display: block; }
  .swoosh__light { fill: var(--band-light); }
  .swoosh__dark  { fill: var(--band-dark); }
  .theme-gold { --band-light: var(--gold-light); --band-dark: var(--gold); }
  .theme-pink { --band-light: var(--pink-light); --band-dark: var(--pink); }
  .theme-blue { --band-light: var(--blue-light); --band-dark: var(--blue); }

  .brand {
    position: absolute; top: 0; background: var(--ink);
    display: flex; align-items: center; justify-content: center;
    color: #fff; font-family: var(--serif); font-weight: 400; letter-spacing: .5px;
  }
  .category {
    position: absolute; font-family: var(--serif); font-weight: 700;
    letter-spacing: 1.6px; color: var(--ink-soft); text-transform: uppercase; white-space: nowrap;
  }
  .product {
    position: absolute; font-family: var(--script); color: var(--ink);
    line-height: 1; white-space: nowrap;
  }
  .note { position: absolute; right: 19px; text-align: right; color: var(--pink-text); font-size: 9.5px; line-height: 1.15; }
  .weight { position: absolute; font-weight: 700; font-size: 9px; }
  .address {
    position: absolute; left: 0; bottom: 0; width: 100%; background: var(--ink); color: #fff;
    display: flex; flex-direction: column; align-items: center; justify-content: center;
    font-size: 6.2px; line-height: 1.55; white-space: nowrap;
  }
  .address strong { font-weight: 700; }
</style>
</head>
<body>

  <!-- Kräuter: Oregano -->
  <section class="label label--oregano theme-gold">
    <svg class="swoosh" style="top:36px;height:76px" viewBox="0 0 200 100" preserveAspectRatio="none" aria-hidden="true">
      <path class="swoosh__light" d="M0,0 C60,20 140,35 200,40 L200,75 C140,80 60,90 0,100 Z"/>
      <path class="swoosh__dark" d="M0,42 C70,48 140,52 200,55 L200,66 C140,69 70,72 0,80 Z"/>
    </svg>
    <div class="brand" style="left:43px;width:102px;height:60px;font-size:13px">Kelmbach</div>
    <p class="category" style="left:20px;top:80px;font-size:8.5px">Kräuter</p>
    <p class="product" style="left:30px;top:104px;font-size:36px;transform:rotate(-8deg)">Oregano</p>
    <p class="weight" style="right:17px;top:158px">200g</p>
    <footer class="address" style="height:28px">
      <span>Lindenweg 7 · 95299 Falkenau · Tel. +49 9000-4812</span>
      <strong>www.kelmbach-tee.de</strong>
    </footer>
  </section>

  <!-- Kräuter & Gewürze: Salbei-Blätter -->
  <section class="label label--salbei theme-gold">
    <svg class="swoosh" style="top:66px;height:96px" viewBox="0 0 200 100" preserveAspectRatio="none" aria-hidden="true">
      <path class="swoosh__light" d="M0,0 C60,20 140,35 200,40 L200,75 C140,80 60,90 0,100 Z"/>
      <path class="swoosh__dark" d="M0,22 C70,34 140,44 200,50 L200,64 C140,68 70,74 0,84 Z"/>
    </svg>
    <div class="brand" style="left:44px;width:105px;height:83px;font-size:14px">Kelmbach</div>
    <p class="category" style="left:21px;top:122px;font-size:8.5px">Kräuter &amp; Gewürze</p>
    <p class="product" style="left:36px;top:168px;font-size:38px;transform:rotate(-10deg)">Salbei-</p>
    <p class="product" style="left:46px;top:210px;font-size:38px;transform:rotate(-10deg)">Blätter</p>
    <p class="weight" style="right:18px;top:273px">200g</p>
    <footer class="address" style="height:38px;font-size:6.5px">
      <span>Lindenweg 7 · 95299 Falkenau · Tel. +49 9000-4812</span>
      <strong>www.kelmbach-tee.de</strong>
    </footer>
  </section>

  <!-- Rooibusch Tee: Vanille -->
  <section class="label label--vanille theme-pink">
    <svg class="swoosh" style="top:36px;height:84px" viewBox="0 0 200 100" preserveAspectRatio="none" aria-hidden="true">
      <path class="swoosh__light" d="M0,0 C60,20 140,35 200,40 L200,75 C140,80 60,90 0,100 Z"/>
      <path class="swoosh__dark" d="M0,36 C70,44 140,50 200,54 L200,68 C140,72 70,76 0,84 Z"/>
    </svg>
    <div class="brand" style="left:46px;width:109px;height:64px;font-size:13.5px">Kelmbach</div>
    <p class="category" style="left:18px;top:87px;font-size:8.5px">Rooibusch Tee</p>
    <p class="product" style="left:38px;top:102px;font-size:40px;transform:rotate(-10deg)">Vanille</p>
    <p class="note" style="top:147px">Roibusch-Tee<br>mit Vanille Geschmack</p>
    <p class="weight" style="right:19px;top:171px">200g</p>
    <footer class="address" style="height:30px">
      <span>Lindenweg 7 · 95299 Falkenau · Tel. +49 9000-4812</span>
      <strong>www.kelmbach-tee.de</strong>
    </footer>
  </section>

  <!-- Bonbons: Fruchtige Seidenkissen -->
  <section class="label label--bonbon theme-blue">
    <svg class="swoosh" style="top:38px;height:84px" viewBox="0 0 200 100" preserveAspectRatio="none" aria-hidden="true">
      <path class="swoosh__light" d="M0,0 C60,20 140,35 200,40 L200,75 C140,80 60,90 0,100 Z"/>
      <path class="swoosh__dark" d="M0,36 C70,44 140,50 200,54 L200,68 C140,72 70,76 0,84 Z"/>
    </svg>
    <div class="brand" style="left:46px;width:110px;height:48px;font-size:13.5px">Kelmbach</div>
    <p class="product" style="left:36px;top:84px;font-size:30px;transform:rotate(-10deg)">Fruchtige</p>
    <p class="product" style="left:18px;top:118px;font-size:30px;transform:rotate(-10deg)">Seidenkissen</p>
    <p class="weight" style="right:17px;top:171px">200g</p>
    <footer class="address" style="height:31px">
      <span>Lindenweg 7 · 95299 Falkenau · Tel. +49 9000-4812</span>
      <strong>www.kelmbach-tee.de</strong>
    </footer>
  </section>

</body>
</html>
```